Email Signatures

I would like to create a new email signature for my team. The design will be the same for everyone, with only individual details such as name and email changing. You can also see our brand style on our website. https://www.tlmbespokehomes.com.au/

Target Market(s)

Clients for new builds or renovations

Industry/Entity Type

Construction

Colors

Designer to choose colors to be used in the design.

```html
<!DOCTYPE html>
<html lang="en">
<head>
<meta charset="utf-8">
<title>TLM Bespoke Homes – Email Signatures</title>
<link rel="stylesheet" href="https://fonts.googleapis.com/css2?family=Playfair+Display:ital,wght@1,700&family=Roboto:wght@400;500;700&display=swap">
<style>
  :root{
    --board:#dcdcdc;
    --card:#202020;
    --card-deep:#161616;
    --card-soft:#2c2c2c;
    --green:#15994a;
    --white:#ffffff;
    --label:#1c1c1c;
  }
  *{margin:0;padding:0;box-sizing:border-box}
  html,body{width:1200px;height:977px;overflow:hidden;background:var(--board)}
  .board{position:relative;width:1200px;height:977px;font-family:"Roboto",Arial,sans-serif}
  .version-label{
    position:absolute;left:0;width:100%;text-align:center;
    font-family:"Playfair Display",Georgia,serif;font-style:italic;font-weight:700;
    font-size:39px;color:var(--label);letter-spacing:1px;
    text-shadow:2px 3px 4px rgba(0,0,0,.25);
  }
  .version-label.top{top:56px;left:-6px}
  .version-label.bottom{top:878px;left:38px}
  .signature{
    position:absolute;left:111px;width:979px;height:327px;
    background:var(--card);overflow:hidden;
    box-shadow:0 10px 14px rgba(0,0,0,.35);
  }
  .signature.black{top:128px}
  .signature.embossed{top:516px}
  .emboss-field{
    position:absolute;inset:0;
    background:radial-gradient(ellipse at 70% 30%,var(--card-soft),var(--card-deep) 75%);
  }
  .brand{position:absolute;left:80px;top:92px;width:300px;display:flex;align-items:center;gap:14px}
  .brand-square{width:22px;height:22px;background:var(--green);flex:none}
  .brand-name{color:var(--white);font-weight:700;line-height:1.02}
  .brand-name .big{display:block;font-size:92px;letter-spacing:2px}
  .brand-name .small{display:block;font-size:25px;letter-spacing:3.2px;text-transform:uppercase;margin-top:6px}
  .divider{position:absolute;left:489px;top:53px;width:2px;height:220px;background:var(--green)}
  .person{position:absolute;left:587px;top:70px}
  .person-name{font-size:40px;font-weight:700;color:var(--green);line-height:1}
  .person-role{font-size:20px;color:var(--white);margin-top:5px;letter-spacing:.5px}
  .contacts{position:absolute;left:587px;top:166px;list-style:none}
  .contacts li{display:flex;align-items:center;height:26px;color:var(--white);font-size:19.5px;letter-spacing:.6px}
  .contacts svg{width:18px;height:18px;margin-right:10px;flex:none}
  .wave{position:absolute;left:0;top:0}
</style>
</head>
<body>
<div class="board">
  <div class="version-label top">Black Version</div>

  <section class="signature black">
    <div class="brand">
      <div class="brand-name"><span class="big">TLM</span><span class="small">Bespoke Homes</span></div>
      <div class="brand-square"></div>
    </div>
    <div class="divider"></div>
    <div class="person">
      <div class="person-name">Dean Whitford</div>
      <div class="person-role">General Manager</div>
    </div>
    <ul class="contacts">
      <li><svg viewBox="0 0 20 20"><path d="M5 2l3 4-2 2c1 2 3 4 5 5l2-2 4 3-2 3C9 17 3 11 2 4z" fill="var(--green)"/></svg>0400 555 182</li>
      <li><svg viewBox="0 0 20 20"><circle cx="10" cy="10" r="8.5" fill="var(--green)"/><path d="M5 6c2 0 3 2 5 2s1 3-1 4-2 3-3 3" stroke="var(--card)" stroke-width="1.6" fill="none"/></svg>www.tlmbespokehomes.com.au</li>
      <li><svg viewBox="0 0 20 20"><path d="M2 8l8-6 8 6v10H2z" fill="var(--green)"/><path d="M2 8l8 6 8-6" stroke="var(--card)" stroke-width="1.4" fill="none"/></svg>info@tlmbespokehomes.com.au</li>
    </ul>
    <svg class="wave" width="979" height="327" viewBox="0 0 979 327">
      <path d="M0,274 C180,335 430,330 620,296 C760,275 880,268 979,273 L979,286 C880,281 760,286 640,302 C450,335 180,340 0,288Z" fill="var(--white)"/>
      <path d="M0,292 C170,342 420,338 600,308 C740,287 870,283 979,290 L979,327 L0,327Z" fill="var(--green)"/>
      <g fill="none" stroke="var(--white)" stroke-width="1.6">
        <rect x="705" y="295" width="18" height="18" rx="2"/>
        <circle cx="745" cy="304" r="9.5"/>
        <circle cx="776" cy="304" r="9.5"/>
        <circle cx="807" cy="304" r="9.5" fill="var(--white)"/>
        <circle cx="838" cy="304" r="9.5"/>
      </g>
    </svg>
  </section>

  <section class="signature embossed">
    <div class="emboss-field" role="img" aria-label="Dark embossed background of repeated brand tiles"></div>
    <div class="brand">
      <div class="brand-name"><span class="big">TLM</span><span class="small">Bespoke Homes</span></div>
      <div class="brand-square"></div>
    </div>
    <div class="divider"></div>
    <div class="person">
      <div class="person-name">Dean Whitford</div>
      <div class="person-role">General Manager</div>
    </div>
    <ul class="contacts">
      <li><svg viewBox="0 0 20 20"><path d="M5 2l3 4-2 2c1 2 3 4 5 5l2-2 4 3-2 3C9 17 3 11 2 4z" fill="var(--green)"/></svg>0400 555 182</li>
      <li><svg viewBox="0 0 20 20"><circle cx="10" cy="10" r="8.5" fill="var(--green)"/><path d="M5 6c2 0 3 2 5 2s1 3-1 4-2 3-3 3" stroke="var(--card)" stroke-width="1.6" fill="none"/></svg>www.tlmbespokehomes.com.au</li>
      <li><svg viewBox="0 0 20 20"><path d="M2 8l8-6 8 6v10H2z" fill="var(--green)"/><path d="M2 8l8 6 8-6" stroke="var(--card)" stroke-width="1.4" fill="none"/></svg>info@tlmbespokehomes.com.au</li>
    </ul>
    <svg class="wave" width="979" height="327" viewBox="0 0 979 327">
      <path d="M0,274 C180,335 430,330 620,296 C760,275 880,268 979,273 L979,286 C880,281 760,286 640,302 C450,335 180,340 0,288Z" fill="var(--white)"/>
      <path d="M0,292 C170,342 420,338 600,308 C740,287 870,283 979,290 L979,327 L0,327Z" fill="var(--green)"/>
      <g fill="none" stroke="var(--white)" stroke-width="1.6">
        <rect x="705" y="295" width="18" height="18" rx="2"/>
        <circle cx="745" cy="304" r="9.5"/>
        <circle cx="776" cy="304" r="9.5"/>
        <circle cx="807" cy="304" r="9.5" fill="var(--white)"/>
        <circle cx="838" cy="304" r="9.5"/>
      </g>
    </svg>
  </section>

  <div class="version-label bottom">Embossed Version</div>
</div>
</body>
</html>
```